Packaging label for Multi purpose ointment/balm

I would like to change packaging label (design) for multi purpose ointment (balm) that I have. Name of company is Vela Orin and I named the product (ointment) TUSKLEN. I attached pictures of existing label that i have (first file). The other 3 files are just changes that I was thinking to add. I would like to completely change look (design) of label. I was thinking to remove name TUSKLEN and make it more stand out "multi purpose ointment" instead. But word TUSKLEN can also stay on it if you think that would come out better. I was also thinking to change it to balm instead of ointment.
So I would like on label to stand out:
-multi purpose ointment or balm
-skin
-muscles
-joints
Ointment would be mostly use for skin problems, so I was thinking to add something like: cuts, burns, scrapes,... next to the word "skin".
Please feel free to use creation and completely change the look of label (design), because I want completely different design, and not similar design.
Here is description of multi purpose ointment:
Tusklen is multi purpose ointment with pain relief, anti-inflammatory and other healing properties for skin, muscles and joints. It is all natural, non-gmo, and made from the finest plant-based ingredients.
PURPOSE AND USE
Tusklen is a multi purpose ointment suitable for everyday use. It can be used to treat various injuries and phenomena of the skin such as wounds, sores, ulcers, mastitis, insect bites, burns, whitlow, herpes, aphthae, bruises, blisters and fungal infections with healing effects generally visible within 3 days. Do not apply directly on open wounds. It may be covered with a loosely wrapped sterile bandage that does not inhibit blood circulation. Tusklen also reduces swelling and relieves pain caused by rheumatism, gout, sciatica, arthritis. It can also be applied as a massage balm to improve blood circulation, reduce inflammation of muscles and ligaments, and alleviate back pain, joint pain, shoulder pain and other muscle soreness. For best results, massage affected area several times a day. In addition, the ointment can be used to effectively relieve nasal and upper respiratory congestion (apply around the nose, chest and throat). Tusklen may also be applied as a daily moisturizer to revitalize skin and prevent the formation of stretch marks. After use, the skin is soft and toned.
marlow Market(s)
Stores like brightcart, shopvane, marlow, bulkery, stores with natural products,...
Industry/Entity Type
It Company
Font styles to use
Requirements
Nice to have
- I want completely different design. Not similar design.

```html
<!DOCTYPE html>
<html lang="en">
<head>
<meta charset="UTF-8">
<title>Vela Orin – Multi Purpose Natural Ointment Label</title>
<link href="https://fonts.googleapis.com/css2?family=Cutive+Mono&family=Raleway:wght@700&family=Roboto+Condensed:wght@700&display=swap" rel="stylesheet">
<style>
  :root {
    --stage: #161616;
    --label-navy: #1f3d55;
    --cap-white: #ffffff;
    --ink-white: #ffffff;
    --brand-ink: #1f2f44;
    --accent-teal: #14a896;
  }
  html, body {
    margin: 0;
    padding: 0;
    width: 1200px;
    height: 909px;
    overflow: hidden;
    background: var(--stage);
  }
  .canvas {
    position: relative;
    width: 1200px;
    height: 909px;
  }
  .label {
    position: absolute;
    left: 100px;
    top: 317px;
    width: 720px;
    height: 197px;
    transform: scale(1.3889);
    transform-origin: top left;
    background: var(--label-navy);
    font-family: "Cutive Mono", "Courier New", monospace;
    color: var(--ink-white);
  }
  .label__cap {
    position: absolute;
    left: 0;
    top: 0;
    width: 720px;
    height: 35px;
    background: var(--cap-white);
  }
  .brand-name {
    position: absolute;
    left: 184px;
    top: 6px;
    margin: 0;
    font-family: "Raleway", Arial, sans-serif;
    font-weight: 700;
    font-size: 22px;
    line-height: 26px;
    color: var(--brand-ink);
  }
  .tagline {
    position: absolute;
    left: 180px;
    width: 350px;
    top: 38px;
    margin: 0;
    text-align: center;
    font-size: 16px;
    line-height: 20px;
    white-space: nowrap;
  }
  .rule {
    position: absolute;
    height: 0;
  }
  .rule--dotted {
    left: 205px;
    width: 298px;
    top: 61px;
    border-top: 1.5px dotted var(--ink-white);
  }
  .rule--dashed {
    left: 189px;
    width: 333px;
    top: 115px;
    border-top: 1px dashed var(--ink-white);
  }
  .headline {
    position: absolute;
    margin: 0;
    font-weight: 400;
    font-size: 46px;
    line-height: 48px;
    letter-spacing: 0.4px;
    white-space: nowrap;
  }
  .headline--upper {
    left: 189px;
    top: 63px;
  }
  .headline--lower {
    left: 274px;
    top: 114px;
  }
  .product-badge {
    position: absolute;
    left: 445px;
    top: 136px;
    width: 77px;
    height: 21px;
    border-radius: 3px;
    background: var(--accent-teal);
    font-family: "Roboto Condensed", Arial, sans-serif;
    font-weight: 700;
    font-size: 14px;
    line-height: 21px;
    text-align: center;
    color: var(--ink-white);
  }
  .uses-badge {
    position: absolute;
    left: 278px;
    top: 160px;
    width: 156px;
    height: 16px;
    background: var(--accent-teal);
    font-size: 13px;
    line-height: 16px;
    text-align: center;
    white-space: nowrap;
    margin: 0;
  }
  .net-volume {
    position: absolute;
    left: 278px;
    width: 156px;
    top: 177px;
    margin: 0;
    text-align: center;
    font-size: 10px;
    line-height: 14px;
    white-space: nowrap;
  }
</style>
</head>
<body>
  <main class="canvas">
    <section class="label" aria-label="Vela Orin ointment tin label">
      <div class="label__cap"></div>
      <p class="brand-name">Vela Orin</p>
      <p class="tagline">multi purpose natural ointment</p>
      <div class="rule rule--dotted"></div>
      <h1 class="headline headline--upper">MUSCLE, SKIN</h1>
      <div class="rule rule--dashed"></div>
      <h2 class="headline headline--lower">JOINTS</h2>
      <span class="product-badge">TUSKLEN</span>
      <p class="uses-badge">Cuts, Burns, Scrapes</p>
      <p class="net-volume">2.54 oz. / 75 ml</p>
    </section>
  </main>
</body>
</html>
```